BIX Promotional flyer for students

We're looking for an 8.5" x 11" flyer that will be distributed to schools. Please see language to include in attached files.

Target Market(s)

The parents and teachers of high school students

Industry/Entity Type

Mental health

Other font styles liked:
• Monserrat and Roboto Slab

Requirements
Must have
• See attached pdf for language to be included on the flyer. Please use the color palette from our website: www.bixzone.tv. Please include some imagery of students. Please ensure the
Nice to have
• Feel free to use any of the graphics provided. See our website for our brand look & feel: www.bixzone.tv

```html
<!DOCTYPE html>
<html lang="en">
<head>
<meta charset="utf-8">
<title>BIX Fundraising Flyer</title>
<link href="https://fonts.googleapis.com/css2?family=Montserrat:wght@300;400;600;700;800&family=Roboto+Slab:wght@700&display=swap" rel="stylesheet">
<style>
  :root {
    --navy: #24305a;
    --orange: #f28a30;
    --orange-bright: #f7891f;
    --teal: #6aa9a8;
    --blue: #5b93b9;
    --blue-dark: #2f6d98;
    --blue-light: #8fc3df;
    --peach: #f8cbb0;
    --paper: #fbfbfb;
    --bg: #ececec;
  }
  * { margin: 0; padding: 0; box-sizing: border-box; }
  html, body { width: 1200px; height: 3020px; overflow: hidden; }
  body { background: var(--bg); position: relative; font-family: "Montserrat", sans-serif; }

  .flyer {
    position: absolute;
    width: 820px; height: 1061px;
    background: var(--paper);
    overflow: hidden;
    box-shadow: 0 6px 18px rgba(0,0,0,.18);
  }
  .flyer--upper { left: 200px; top: 235px; transform-origin: 0 0; transform: scale(0.975); }
  .flyer--lower { left: 190px; top: 1760px; }

  .corner-band { position: absolute; left: 370px; top: 0; width: 450px; height: 230px; }
  .corner-blob { position: absolute; left: 0; top: 890px; width: 160px; height: 171px; }

  .brand { position: absolute; left: 45px; top: 70px; display: flex; align-items: center; gap: 14px; }
  .brand__dot { width: 62px; height: 62px; border-radius: 50%; background: var(--orange); }
  .brand__name { font-weight: 800; font-size: 64px; color: var(--orange); letter-spacing: -1px; line-height: 1; }

  .headline { position: absolute; left: 45px; top: 208px; font-weight: 800; font-size: 50px; line-height: 1.05; }
  .headline__top { color: var(--navy); display: block; }
  .headline__bottom { color: var(--orange); display: block; }

  .stat { position: absolute; left: 40px; top: 318px; font-weight: 700; font-size: 142px; color: var(--navy); letter-spacing: -5px; line-height: 1; }
  .stat-note { position: absolute; left: 45px; top: 458px; font-family: "Roboto Slab", serif; font-weight: 700; font-size: 22px; color: var(--navy); line-height: 1.2; }

  .photo { position: absolute; border: 5px solid #fff; }
  .photo--mentor {
    left: 368px; top: 80px; width: 420px; height: 452px;
    border-radius: 0 0 0 120px;
    background: linear-gradient(135deg, #ece6da 0%, #d9c9a6 35%, #e9b23a 60%, #c7893a 80%, #7b8fae 100%);
  }
  .photo--game {
    left: 42px; top: 568px; width: 348px; height: 390px;
    border-radius: 0 0 120px 0;
    background: linear-gradient(135deg, #c9cbc7 0%, #6fb7ab 35%, #2f5e4a 55%, #e9ded2 75%, #b68d62 100%);
  }

  .section-title { position: absolute; left: 412px; top: 586px; font-weight: 700; font-size: 42px; line-height: 1.05; color: var(--navy); }
  .section-title__accent { color: var(--teal); display: block; }

  .blurb { position: absolute; left: 410px; top: 750px; padding-left: 32px; }
  .blurb::before { content: ""; position: absolute; left: 0; top: 4px; width: 10px; height: 138px; background: var(--orange); }
  .blurb p { font-weight: 400; font-size: 19px; line-height: 24.5px; color: var(--navy); white-space: nowrap; }

  .peach-corner { position: absolute; left: 630px; top: 872px; width: 160px; height: 156px; }

  .site-pill {
    position: absolute; left: 259px; top: 983px; width: 303px; height: 44px;
    background: var(--orange); border-radius: 22px 22px 0 0;
    color: #fff; font-size: 19px; font-weight: 300; letter-spacing: .5px;
    display: flex; align-items: center; justify-content: center;
  }
  .site-pill strong { font-weight: 700; }
</style>
</head>
<body>

<article class="flyer flyer--upper">
  <svg class="corner-band" viewBox="0 0 450 230" aria-hidden="true">
    <rect x="0" y="0" width="450" height="80" fill="var(--orange-bright)"/>
    <circle cx="40" cy="35" r="50" fill="var(--blue-dark)"/>
    <circle cx="140" cy="0" r="70" fill="var(--blue-light)"/>
    <circle cx="430" cy="45" r="70" fill="var(--blue)"/>
    <circle cx="395" cy="0" r="50" fill="var(--blue-dark)"/>
    <rect x="430" y="80" width="20" height="150" fill="var(--teal)"/>
  </svg>
  <svg class="corner-blob" viewBox="0 0 160 171" aria-hidden="true">
    <circle cx="40" cy="120" r="115" fill="var(--blue)"/>
  </svg>

  <div class="brand"><span class="brand__dot"></span><span class="brand__name">bix</span></div>
  <h1 class="headline"><span class="headline__top">FUNDRAISE</span><span class="headline__bottom">WITH BIX</span></h1>
  <div class="stat">50%</div>
  <p class="stat-note">OF ALL PROCEEDS GO BACK<br>TO YOUR SCHOOL</p>

  <div class="photo photo--mentor" role="img" aria-label="Photo of a counsellor in a yellow cardigan talking with a girl holding a teddy bear"></div>
  <div class="photo photo--game" role="img" aria-label="Photo of a teacher and a student playing a word tile game at a table"></div>

  <h2 class="section-title">Support the<br>mental health<span class="section-title__accent">of your students</span></h2>
  <div class="blurb"><p>BIX is a simple and effective<br>way to improve mental health.<br>Your students will learn valuable<br>coping skills and techniques<br>from expert clinicians who<br>analyze real cases and share<br>their insights and advice.</p></div>

  <svg class="peach-corner" viewBox="0 0 160 156" aria-hidden="true"><polygon points="160,0 160,156 0,156" fill="var(--peach)"/></svg>
  <div class="site-pill">WWW.<strong>BIXZONE</strong>.TV</div>
</article>

<article class="flyer flyer--lower">
  <svg class="corner-band" viewBox="0 0 450 230" aria-hidden="true">
    <rect x="0" y="0" width="450" height="80" fill="var(--orange-bright)"/>
    <circle cx="40" cy="35" r="50" fill="var(--blue-dark)"/>
    <circle cx="140" cy="0" r="70" fill="var(--blue-light)"/>
    <circle cx="430" cy="45" r="70" fill="var(--blue)"/>
    <circle cx="395" cy="0" r="50" fill="var(--blue-dark)"/>
    <rect x="430" y="80" width="20" height="150" fill="var(--teal)"/>
  </svg>
  <svg class="corner-blob" viewBox="0 0 160 171" aria-hidden="true">
    <circle cx="40" cy="120" r="115" fill="var(--blue)"/>
  </svg>

  <div class="brand"><span class="brand__dot"></span><span class="brand__name">bix</span></div>
  <h1 class="headline"><span class="headline__top">FUNDRAISE</span><span class="headline__bottom">WITH BIX</span></h1>
  <div class="stat">50%</div>
  <p class="stat-note">OF ALL PROCEEDS GO BACK<br>TO YOUR SCHOOL</p>

  <div class="photo photo--mentor" role="img" aria-label="Photo of a counsellor in a yellow cardigan talking with a girl holding a teddy bear"></div>
  <div class="photo photo--game" role="img" aria-label="Photo of a teacher and a student playing a word tile game at a table"></div>

  <h2 class="section-title">Support the<br>mental health<span class="section-title__accent">of your students</span></h2>
  <div class="blurb"><p>BIX is a simple and effective<br>way to improve mental health.<br>Your students will learn valuable<br>coping skills and techniques<br>from expert clinicians who<br>analyze real cases and share<br>their insights and advice.</p></div>

  <svg class="peach-corner" viewBox="0 0 160 156" aria-hidden="true"><polygon points="160,0 160,156 0,156" fill="var(--peach)"/></svg>
  <div class="site-pill">WWW.<strong>BIXZONE</strong>.TV</div>
</article>

</body>
</html>
```